Creative web design needed for a Labour Hire business

About the business
The website is for a professional labor hire services business.
The business is responsible for recruiting temporary,casual and full time workers for all sectors including building industry, general office administrators, factory workers etc...

About the design work required
We have purchased a template located at http://preview07.layoutvault-demo.com/wordpress_58126 and would like a designer to add some further creativity to the design.
We would like to use this design as our base for this project. We can provide the full PSD in order for you to use as a based for the design.

In general the design looks good but the client is not 100% happy with it. The client did like the look and feel (especially the footer) but was not happy with the masthead and slider. We would like to see some variations of the header - the current one looks too simple and too much like a "template".

Things we like about the design
- Footer looks good.
- General look and feel is clean and simple - which is what we want.

Things we do not like about the design
- Do not like the header. The top area that contains the logo and navigation looks too simple and boring. The height of the logo and navigation seems too small and dull.
- Do not like the the slider look. We need a slider that is the full width of the content like brolvarin.edu.au and quastiply.com

Please use sample images for the slider and we can add some further images at a later point.
- Colour does not match the logo - we need it to match the colour of the logo

Sites that we like
www.brolvarin.edu.au
We do like the header and footer colours and look/feel.
The right panel looks good as well.
www.quastiply.com/
Slider looks good
Background image (the transparent boxes) is nice and appealing.

PSD and logo can be downloaded from the below location
http://files.stowbinbox.net/u/8830467/design.zip

I would like to see a quote and a list of your most recent work.

I am willing to move quickly with this and get the design completed asap.

Target Market(s)

Businesses that require labour workers and also workers looking for a job

Industry/Entity Type

Business

Requirements
Must have
• - The design must look modern and professional.
- An image slider is a must have.
- Website colours must match the blue and white as per the logo.
- A right panel that displays get a quote form (form includes firstname, lastname, email, phone, message) and / or testimonials is required.
- Site should be 100% width. Main content to be about 920px - see PSD for exact dimensions.
- Footer should be 4 columns to include testimonials, services, page and either a contact us form or search form - as per the current PSD.
Should not have
• - We DO NOT required a new website design - we have a based PSD design and would like to improve it and add some further creativity to the existing design.
- Do not use bland or old designs. We need something modern and professional.
- We do not want a template feel to the design. We want some customization.
- NO HTML/CSS is required. Just an PSD file.

```html
<!DOCTYPE html>
<html lang="en">
<head>
<meta charset="utf-8">
<title>Steadfast Staffing – Labour Hire</title>
<link href="https://fonts.googleapis.com/css2?family=Open+Sans:ital,wght@0,400;0,600;0,700;0,800;1,400&display=swap" rel="stylesheet">
<style>
:root{
  --blue:#1c9be0;
  --blue-dark:#0d6fb5;
  --blue-deep:#0a5a96;
  --navy:#222a33;
  --nav:#2b2f34;
  --ink:#2a2e33;
  --muted:#6d737a;
  --line:#d9dde1;
  --page:#eef1f4;
  --white:#ffffff;
  --logo-strip:#e4e7ea;
}
*{box-sizing:border-box;margin:0;padding:0}
html,body{width:893px;height:1200px;overflow:hidden}
body{font-family:"Open Sans",Arial,sans-serif;color:var(--ink);background:var(--page);position:relative;font-size:11px}
.wrap{position:absolute;left:107px;width:680px}

/* header */
.masthead{position:absolute;left:0;top:0;width:893px;height:92px;background:var(--white)}
.brand{position:absolute;left:107px;top:18px;display:flex;align-items:center;gap:10px}
.brand-mark{width:46px;height:46px;background:var(--navy)}
.brand-name{font-weight:800;font-size:27px;line-height:1;color:var(--navy);letter-spacing:.5px}
.brand-name small{display:block;font-size:16px;font-weight:800;letter-spacing:0;margin-top:2px}
.contact{position:absolute;right:106px;top:22px;text-align:right}
.contact .phone{font-size:22px;color:var(--navy);display:flex;align-items:center;gap:8px;justify-content:flex-end}
.contact .email{font-size:12px;color:var(--muted);margin-top:6px;display:flex;align-items:center;gap:6px;justify-content:flex-end}

.navbar{position:absolute;left:0;top:92px;width:893px;height:34px;background:var(--nav);border-top:3px solid #1a1d21}
.navbar ul{list-style:none;position:absolute;left:107px;top:0;display:flex;height:31px}
.navbar li{color:#d8dde2;font-size:10px;font-weight:700;padding:0 24px;line-height:31px;border-right:1px solid #3b4046}
.navbar li.active{background:var(--blue);color:var(--white)}
.login{position:absolute;right:106px;top:5px;background:var(--blue);color:var(--white);font-size:10px;font-weight:600;padding:4px 12px 4px 24px;border-radius:2px}
.login:before{content:"";position:absolute;left:9px;top:7px;width:8px;height:8px;border-radius:50%;background:var(--white)}

/* slider */
.slider{top:138px;height:280px;border:5px solid var(--white);box-shadow:0 1px 4px rgba(0,0,0,.2)}
.slide-photo{width:100%;height:100%;background:linear-gradient(120deg,#c7d5de 0%,#e9edf1 45%,#b9c3cb 70%,#8a99a6 100%)}
.caption{position:absolute;left:0;bottom:18px;width:72%;background:rgba(20,24,30,.72);color:var(--white);padding:8px 14px}
.caption h2{font-size:17px;font-weight:600;font-style:italic}
.caption p{font-size:9px;color:#cfd5db;margin-top:3px;line-height:1.35}
.slider-arrows{position:absolute;right:12px;bottom:26px;display:flex;gap:4px}
.slider-arrows span{width:20px;height:20px;background:rgba(20,24,30,.75);color:var(--white);font-size:10px;text-align:center;line-height:20px}

/* news */
.news{top:438px;height:52px;background:var(--white);border-top:1px solid var(--line);border-bottom:1px solid var(--line);display:flex;align-items:center;padding:0 8px}
.news h3{font-size:15px;font-style:italic;font-weight:700;width:108px}
.news .chev{font-size:22px;color:var(--ink);padding:0 8px}
.news p{flex:1;font-size:9px;line-height:1.4;color:var(--muted)}
.news p b{color:var(--ink)}

/* content */
.feature{position:absolute;top:512px;width:210px}
.feature h4{font-size:15px;font-weight:400;margin-bottom:8px}
.feature .thumb{height:96px;border:3px solid var(--white);box-shadow:0 1px 3px rgba(0,0,0,.2)}
.feature p{font-size:8.5px;line-height:1.45;color:var(--muted);margin-top:10px}
.feature p b{color:var(--ink)}
.more{display:inline-block;margin-top:12px;background:var(--navy);color:var(--white);font-size:8px;font-weight:700;padding:4px 8px}
.feature-consult{left:107px}
.feature-analysis{left:342px}

.quote{position:absolute;left:583px;top:512px;width:204px;height:290px;background:var(--white);border:1px solid var(--line)}
.quote h4{background:var(--blue);color:var(--white);text-align:center;font-size:14px;font-weight:600;padding:6px 0}
.quote form{padding:8px 12px}
.field{height:18px;border:1px solid var(--line);font-size:8px;color:var(--muted);padding:3px 5px;margin-bottom:5px}
.field.msg{height:100px}
.submit{display:block;margin:6px auto 0;background:var(--blue-dark);color:var(--white);font-size:8px;font-weight:700;padding:5px 14px;width:max-content}

/* clients */
.clients{position:absolute;left:0;top:820px;width:893px;height:64px;background:var(--logo-strip);display:flex;justify-content:center;align-items:center;gap:40px}
.clients span{font-size:15px;font-weight:700;color:#b6bcc2}

/* footer */
.footer{position:absolute;left:0;top:884px;width:893px;height:276px;background:linear-gradient(#2aa6e8,var(--blue-dark))}
.fcol{position:absolute;top:30px;color:var(--white)}
.fcol h5{font-size:16px;font-weight:400;margin-bottom:14px}
.fcol p{font-size:8.5px;line-height:1.45;color:#dcefff}
.fcol p.by{color:var(--white);font-weight:600;margin:3px 0 14px}
.fcol ul{list-style:none}
.fcol li{font-size:8.5px;color:#e6f4ff;padding:5px 0 5px 10px;border-bottom:1px solid rgba(255,255,255,.2);position:relative}
.fcol li:before{content:"";position:absolute;left:0;top:9px;width:4px;height:4px;background:var(--white)}
.help{position:absolute;left:620px;top:20px;width:167px;background:var(--blue-deep);padding:10px;text-align:center;color:var(--white)}
.help h6{font-size:11px;font-weight:600}
.help .sub{font-size:8px;color:#cfe8fb}
.help .num{font-size:20px;font-weight:600;margin-top:4px}
.social{position:absolute;left:620px;top:114px;width:167px}
.social div{display:flex;align-items:center;gap:8px;font-size:9px;color:var(--white);padding:6px 0;border-bottom:1px solid rgba(255,255,255,.2)}
.social i{width:14px;height:14px;border-radius:50%;background:var(--white);display:block}

.bottom{position:absolute;left:0;top:1160px;width:893px;height:40px;background:var(--white);font-size:9px;color:var(--muted)}
.bottom .copy{position:absolute;left:107px;top:14px}
.bottom .links{position:absolute;right:106px;top:14px}
</style>
</head>
<body>

<header class="masthead">
  <div class="brand">
    <span class="brand-mark"></span>
    <div class="brand-name">STEADFAST<small>Staffing</small></div>
  </div>
  <div class="contact">
    <div class="phone">
      <svg width="20" height="18" viewBox="0 0 20 18"><rect x="1" y="2" width="18" height="14" rx="3" fill="#1c9be0"/><path d="M6 6c1 4 4 6 8 7l1-2-2-1-1 1c-2-1-3-2-4-4l1-1-1-2z" fill="#fff"/></svg>
      1300 555 018
    </div>
    <div class="email">
      <svg width="14" height="10" viewBox="0 0 14 10"><rect width="14" height="10" rx="1" fill="#1c9be0"/><path d="M1 1l6 5 6-5" stroke="#fff" fill="none"/></svg>
      info@steadfaststaffing.com
    </div>
  </div>
</header>

<nav class="navbar">
  <ul>
    <li class="active">HOME</li><li>COMPANY</li><li>SERVICES</li><li>CLIENTS</li><li>CONTACTS</li>
  </ul>
  <span class="login">Client login</span>
</nav>

<section class="wrap slider">
  <div class="slide-photo" role="img" aria-label="Photo of a smiling business team in a bright office"></div>
  <div class="caption">
    <h2>Solutions, that you need!</h2>
    <p>We match skilled temporary, casual and full time workers with businesses across every sector.</p>
  </div>
  <div class="slider-arrows"><span>&#9664;</span><span>&#9654;</span></div>
</section>

<section class="wrap news">
  <h3>Latest News:</h3>
  <span class="chev">&#8249;</span>
  <p><b>New building industry contracts open this month.</b> Register today to join our casual labour team and start work within days across the metro region.</p>
  <span class="chev">&#8250;</span>
</section>

<div class="feature feature-consult">
  <h4>Consultation</h4>
  <div class="thumb" role="img" aria-label="Photo of a consultant in a business shirt" style="background:linear-gradient(135deg,#7f8c96,#d4dae0 60%,#a8b2ba)"></div>
  <p><b>Our consultants</b> assess your staffing needs and build a workforce plan that fits your project, budget and timeline.</p>
  <span class="more">MORE</span>
</div>
<div class="feature feature-analysis">
  <h4>Analysis</h4>
  <div class="thumb" role="img" aria-label="Photo of hands typing on a keyboard" style="background:linear-gradient(135deg,#5d6f80,#b5c3cf 55%,#7d8e9c)"></div>
  <p><b>We review skills</b>, safety records and references so every worker we place is ready from day one.</p>
  <span class="more">MORE</span>
</div>

<aside class="quote">
  <h4>Get a Quote</h4>
  <form>
    <div class="field">First Name:</div>
    <div class="field">Last Name:</div>
    <div class="field">Email:</div>
    <div class="field">Phone:</div>
    <div class="field msg">Message:</div>
    <span class="submit">SUBMIT</span>
  </form>
</aside>

<div class="clients">
  <span>Verolt</span><span>Nexagrid</span><span>Plumwell</span><span>Corvane</span><span>Tallwick</span>
</div>

<footer class="footer">
  <div class="fcol" style="left:107px;width:150px">
    <h5>Testimonials</h5>
    <p>Fast, reliable staff every time. Our site never waits for workers.</p>
    <p class="by">By Happy Client</p>
    <p>The team found office staff in two days. Highly recommended.</p>
    <p class="by">By Happy Client</p>
  </div>
  <div class="fcol" style="left:285px;width:140px">
    <h5>Services</h5>
    <ul>
      <li>Management Consulting</li><li>Office and Factory Staffing</li><li>Market Assessment</li>
      <li>Program Management</li><li>Regulation Support</li><li>Labour Hire and Risk Assessment</li>
    </ul>
  </div>
  <div class="fcol" style="left:455px;width:140px">
    <h5>Pages</h5>
    <ul>
      <li>Home</li><li>About Company</li><li>Frequently Asked Questions</li>
      <li>Career</li><li>Online Support</li><li>Useful Links</li>
    </ul>
  </div>
  <div class="help">
    <h6>Need Help or Advice?</h6>
    <div class="sub">Call Now &amp; Get Instant Solution</div>
    <div class="num">1300 555 018</div>
  </div>
  <div class="social">
    <div><i></i>Follow us online</div>
    <div><i></i>Connect with us</div>
    <div><i></i>Find us on social</div>
  </div>
</footer>

<div class="bottom">
  <span class="copy">Steadfast Staffing (c) 2011 &nbsp;|&nbsp; Privacy policy</span>
  <span class="links">Home &nbsp;|&nbsp; Company &nbsp;|&nbsp; Services &nbsp;|&nbsp; Clients &nbsp;|&nbsp; Contacts</span>
</div>

</body>
</html>
```